Forest Consultant/Timber Buyer needs a clean business card

We are a forestry consulting and timber buying company. We meet with private landowners and assist them with timber management and timber harvesting. We would like a professional business card, please no clip art. logo is blue and white but would like to see a gray,silver, or some other color incorporated. Would like basic contact info. Would like to the layout to be creative and sleek but masculine.

Target Market(s)

private landowners

Industry/Entity Type

Business

Contact Information for Business Card

name,position, cell number, office number, email, website. This might be to cluttered. Basic contact info is what we are looking for.

Contact info can all be on one side with logo on the other.

Font styles to use
Serif
Sans Serif

Colors
0255a3
ffffff
aaaaaa

Requirements
Must have
• We just want it professional.
Nice to have
• Creative layout.
Should not have
• please no clip art of log trucks etc.

```html
<!DOCTYPE html>
<html lang="en">
<head>
<meta charset="utf-8">
<title>Northridge Land &amp; Timber – Business Card</title>
<link href="https://fonts.googleapis.com/css2?family=Saira+Semi+Condensed:wght@600&family=Source+Sans+3:wght@400&display=swap" rel="stylesheet">
<style>
  :root{
    --brand-blue:#0f4f96;
    --white:#ffffff;
    --silver:#6d6b6b;
    --light-silver:#aaaaaa;
    --paper:#f7f7f6;
    --ink:#555555;
    --backdrop:#a9a7a7;
  }
  *{margin:0;padding:0;box-sizing:border-box;}
  html,body{width:1200px;height:1200px;overflow:hidden;background:var(--backdrop);}
  .canvas{position:relative;width:1200px;height:1200px;}

  .card{position:absolute;overflow:hidden;}
  .card--front{left:237px;top:116px;width:714px;height:422px;background:var(--brand-blue);}
  .card--back{left:229px;top:644px;width:715px;height:417px;background:var(--paper);}

  .brand{position:absolute;display:flex;align-items:center;gap:18px;
    font-family:"Saira Semi Condensed",sans-serif;font-weight:600;line-height:1;white-space:nowrap;}
  .brand__dot{border-radius:50%;flex:none;}

  .card--front .brand{left:0;right:0;top:182px;justify-content:center;color:var(--white);font-size:44px;}
  .card--front .brand__dot{width:46px;height:46px;background:var(--white);}

  .card--back .brand{left:47px;top:66px;color:var(--brand-blue);font-size:36px;}
  .card--back .brand__dot{width:38px;height:38px;background:var(--brand-blue);}

  .waves{position:absolute;left:0;top:0;width:715px;height:417px;}

  .contact{position:absolute;left:47px;top:184px;font-family:"Source Sans 3",sans-serif;color:var(--ink);}
  .contact__address{font-size:19px;margin-bottom:10px;}
  .contact__list{list-style:none;}
  .contact__item{display:flex;align-items:center;gap:18px;font-size:19px;height:27px;}
  .contact__icon{width:18px;height:18px;flex:none;}

  .person{position:absolute;right:40px;top:318px;text-align:right;color:var(--white);}
  .person__name{font-family:"Saira Semi Condensed",sans-serif;font-weight:600;font-size:29px;line-height:1;}
  .person__title{font-family:"Source Sans 3",sans-serif;font-size:18px;margin-top:8px;}
</style>
</head>
<body>
<main class="canvas">

  <section class="card card--front" aria-label="Card front">
    <div class="brand">
      <span class="brand__dot"></span>
      <span class="brand__name">Northridge Land &amp; Timber</span>
    </div>
  </section>

  <section class="card card--back" aria-label="Card back">
    <svg class="waves" viewBox="0 0 715 417" aria-hidden="true">
      <path fill="var(--brand-blue)" d="M715,229 C560,236 480,300 380,338 C280,378 110,392 0,370 L0,417 L715,417 Z"/>
      <path fill="var(--silver)" d="M715,203 C540,206 470,268 380,306 C260,356 110,366 0,340 L0,360 C120,384 270,374 380,326 C480,284 560,222 715,216 Z"/>
      <path fill="none" stroke="var(--light-silver)" stroke-width="3" d="M62,346 C180,358 300,354 400,330"/>
    </svg>

    <div class="brand">
      <span class="brand__dot"></span>
      <span class="brand__name">Northridge Land &amp; Timber</span>
    </div>

    <div class="contact">
      <p class="contact__address">Your Long Commercial or business&nbsp; address in 2 line</p>
      <ul class="contact__list">
        <li class="contact__item">
          <svg class="contact__icon" viewBox="0 0 18 18" aria-hidden="true"><path fill="var(--brand-blue)" d="M1,6 C1,2 17,2 17,6 L17,8 L13,8 L13,6 L5,6 L5,8 L1,8 Z M4,9 L14,9 L16,16 L2,16 Z"/><circle cx="9" cy="12.5" r="2" fill="var(--paper)"/></svg>
          +00 111 222 3333
        </li>
        <li class="contact__item">
          <svg class="contact__icon" viewBox="0 0 18 18" aria-hidden="true"><rect x="1" y="4" width="16" height="11" fill="var(--brand-blue)"/><path d="M1,4 L9,11 L17,4 M1,15 L7,9 M17,15 L11,9" stroke="var(--paper)" stroke-width="1.3" fill="none"/></svg>
          yourname@yourwebsite.com
        </li>
        <li class="contact__item">
          <svg class="contact__icon" viewBox="0 0 18 18" aria-hidden="true"><circle cx="9" cy="9" r="7.5" fill="var(--brand-blue)"/><path d="M1.5,9 H16.5 M9,1.5 V16.5 M3,5 H15 M3,13 H15" stroke="var(--paper)" stroke-width="1" fill="none"/><ellipse cx="9" cy="9" rx="3.5" ry="7.5" stroke="var(--paper)" stroke-width="1" fill="none"/></svg>
          www.yourwebsite.com
        </li>
      </ul>
    </div>

    <div class="person">
      <p class="person__name">Your Good Name</p>
      <p class="person__title">Your Title</p>
    </div>
  </section>

</main>
</body>
</html>
```